Photo/Video Company needs a business card design

We need a business card design for a photo/video production company called 'Brightwave Studios'. We primarily do wedding photography and videography, however we also do commercial, corporate, and promo work.

We would like a clean, white design that primarily markets us as a wedding photo/video company, but still sleek enough that we attract corporate and commercial clients.

Industry/Entity Type

Wedding

Requirements
Must have
• We wish the front of the business card to simply have the logo, and the back will have the contact information:

Brightwave Studios
Wedding, Event, Corporate, Commercial, Promo
647-518-2736
info@brightwavestudios.example
www.brightwavestudios.example

We are hoping for a version of the card that has only the companies name on it, as well as several variations that have different employees names printed.

The employee names and titles are:

Teo Lindqvar - Photo/Video
Dilan Lindqvar - Photo/Video
Pieter Kalbrook -Video
Odile Brunvik -Photo/Video

The design should use similar fonts in the writing as the fonts used in the logo design. The AI file will be provided.
Nice to have
• We also might like to see the front of the card have the main logo, as well as 'Wedding, Event, Corporate, Commercial, Promo' written in the bottom corner.
Should not have
• No old style fonts should be used. Also no other graphic images should be created, but we are open to the possibility of having shapes and borders.

```html
<!DOCTYPE html>
<html lang="en">
<head>
<meta charset="utf-8">
<title>Brightwave Studios – Business Card</title>
<link rel="stylesheet" href="https://fonts.googleapis.com/css2?family=Michroma&display=swap">
<style>
  :root {
    --stage: #cccccc;
    --card: #ffffff;
    --ink: #1c1c1c;
    --ink-soft: #333333;
    --accent: #e0141b;
    --edge-front: #111111;
    --edge-back: #b5b5b5;
  }
  * { box-sizing: border-box; margin: 0; padding: 0; }
  html, body {
    width: 1200px;
    height: 632px;
    overflow: hidden;
    background: var(--stage);
    font-family: "Michroma", sans-serif;
    color: var(--ink);
  }
  .stage {
    position: relative;
    width: 1200px;
    height: 632px;
  }
  .card {
    position: absolute;
    top: 159px;
    width: 533px;
    height: 304px;
    background: var(--card);
  }
  .card--front {
    left: 46px;
    border: 1px solid var(--edge-front);
  }
  .card--back {
    left: 621px;
    border: 1px solid var(--edge-back);
    box-shadow: 1px 1px 2px rgba(0,0,0,0.15);
  }

  /* Front */
  .brand {
    position: absolute;
    left: 40px;
    top: 76px;
    display: flex;
    align-items: center;
    gap: 14px;
  }
  .brand__mark {
    width: 16px;
    height: 16px;
    background: var(--accent);
  }
  .brand__name {
    font-size: 23px;
    letter-spacing: 0.5px;
    color: var(--ink);
    text-transform: uppercase;
    white-space: nowrap;
  }
  .tagline {
    position: absolute;
    left: 160px;
    top: 122px;
    font-size: 10px;
    letter-spacing: 9px;
    color: var(--ink-soft);
  }
  .services {
    position: absolute;
    left: 0;
    right: 0;
    top: 264px;
    display: flex;
    justify-content: center;
    align-items: center;
    gap: 11px;
    font-size: 11.5px;
    letter-spacing: 0.6px;
    color: var(--ink-soft);
    list-style: none;
  }
  .services__sep {
    width: 4px;
    height: 4px;
    background: var(--accent);
  }

  /* Back */
  .contact {
    position: absolute;
    right: 35px;
    top: 230px;
    text-align: right;
    font-size: 14px;
    line-height: 14.5px;
    letter-spacing: 0.8px;
    color: var(--ink);
    font-style: normal;
  }
  .contact__domain { color: var(--accent); }
</style>
</head>
<body>
<main class="stage">
  <section class="card card--front" aria-label="Card front">
    <div class="brand">
      <span class="brand__mark" aria-hidden="true"></span>
      <span class="brand__name">Brightwave Studios</span>
    </div>
    <p class="tagline">photo + cinema</p>
    <ul class="services">
      <li>Wedding</li><li class="services__sep" aria-hidden="true"></li>
      <li>Event</li><li class="services__sep" aria-hidden="true"></li>
      <li>Corporate</li><li class="services__sep" aria-hidden="true"></li>
      <li>Commercial</li><li class="services__sep" aria-hidden="true"></li>
      <li>Promo</li>
    </ul>
  </section>

  <section class="card card--back" aria-label="Card back">
    <address class="contact">
      <div class="contact__phone">647-518-2736</div>
      <div class="contact__email">info@brightwavestudios.example</div>
      <div class="contact__web">www.<span class="contact__domain">brightwavestudios</span>.example</div>
    </address>
  </section>
</main>
</body>
</html>
```